Elegant Business Card for Technology Company

Client is a supplier of innovative industrial communications and automation equipment since 2002. This contest is to gather fresh ideas for a redesign of the existing business card. Client is looking for design that best communicates tagline "Industrial Networking and Computing Specialist".

Design submissions should look modern, clean, elegant and professional. It should not be cluttered. Use white as the primary colour. Orange and black as secondary colour. Refer to jpeg File 1 on the current design.

Fonts used by Client used include Arial Regular, Arial Black, Roboto Regular, Roboto Black and Lato.

The winning design will be sent for offset printing using super white 250gsm artcard paper (open for suggestions).

Target Market(s)

System Engineers, Project Managers, Purchasing Managers from companies providing engineering services for Smart Cities.

Industry/Entity Type

Information Technology

Contact Information for Business Card

Refer to PDF File 3 for Business Card Details. Priority of short contact information would be as follows Name > Job Title > Email > Mobile > Web > Tel > Fax > Business Address >UEN (UEN represents company registration number)

Font styles to use
Sans Serif

Colors
ffffff
f37122
000000
5c5c5c

Requirements
Must have
• Refer to AI File 2 (Company Logo) & PDF File 3 (Information on Namecard)
Should not have
• No QR codes
• No Social Media Icons
• Do not create full Black or Orange colour background

```html
<!DOCTYPE html>
<html lang="en">
<head>
<meta charset="utf-8">
<title>NEXALINK Business Card</title>
<link href="https://fonts.googleapis.com/css2?family=Source+Sans+3:wght@400;600&display=swap" rel="stylesheet">
<style>
  :root {
    --backdrop: #d8d5d1;
    --card: #ffffff;
    --white: #ffffff;
    --ink: #000000;
    --orange: #f37122;
    --grey: #5c5c5c;
    --rule: #c9c9c9;
  }
  * { margin: 0; padding: 0; box-sizing: border-box; }
  html, body { width: 1200px; height: 814px; overflow: hidden; }
  body {
    background: var(--backdrop);
    font-family: "Source Sans 3", Arial, sans-serif;
    color: var(--ink);
    position: relative;
  }
  .card {
    position: absolute;
    top: 257px;
    width: 510px;
    height: 300px;
    background: var(--card);
    border-radius: 3px;
    box-shadow: 0 6px 18px rgba(0,0,0,0.18);
  }
  .card-front { left: 70px; }
  .card-back { left: 620px; }

  /* Front */
  .brand {
    position: absolute;
    left: 58px;
    top: 46px;
    display: flex;
    align-items: center;
    gap: 10px;
  }
  .brand-dot {
    width: 34px; height: 34px;
    border-radius: 50%;
    background: var(--orange);
  }
  .brand-name {
    font-size: 30px;
    font-weight: 600;
    letter-spacing: 1px;
    color: var(--ink);
  }
  .identity {
    position: absolute;
    right: 262px;
    top: 150px;
    text-align: right;
    font-size: 17px;
    line-height: 21px;
    color: var(--grey);
  }
  .person-name {
    color: var(--orange);
    font-size: 21px;
    font-weight: 600;
    line-height: 24px;
  }
  .job-title { color: var(--ink); }
  .divider {
    position: absolute;
    left: 262px;
    top: 130px;
    width: 1px;
    height: 132px;
    background: var(--rule);
  }
  .contacts {
    position: absolute;
    left: 278px;
    top: 132px;
    list-style: none;
    font-size: 16px;
    line-height: 22px;
    color: var(--grey);
  }
  .contacts li { display: flex; align-items: center; gap: 9px; }
  .contacts svg { width: 13px; height: 13px; flex: none; fill: var(--orange); }

  /* Back */
  .back-mark {
    position: absolute;
    left: 50%;
    top: 36px;
    transform: translateX(-50%);
    width: 118px; height: 118px;
    border-radius: 50%;
    background: var(--orange);
    display: flex;
    align-items: center;
    justify-content: center;
  }
  .back-mark .brand-name { font-size: 22px; color: var(--white); }
  .tagline {
    position: absolute;
    left: 0; right: 0;
    top: 176px;
    text-align: center;
    list-style: none;
    font-size: 15px;
    line-height: 20px;
    color: var(--grey);
  }
  .tagline .lead { color: var(--ink); font-weight: 600; }
</style>
</head>
<body>
  <section class="card card-front">
    <div class="brand">
      <span class="brand-dot"></span>
      <span class="brand-name">NEXALINK</span>
    </div>

    <div class="identity">
      <p class="person-name">Adrian Tan</p>
      <p class="job-title">Sales Manager</p>
      <p>24 Harbour Lane</p>
      <p>Eastgate Park #02-15 (Block B)</p>
      <p>Singapore 400123</p>
    </div>

    <div class="divider"></div>

    <ul class="contacts">
      <li>
        <svg viewBox="0 0 16 16" aria-hidden="true"><path d="M3 1h3l1.5 4-2 1.3a9 9 0 0 0 4.2 4.2L11 8.5l4 1.5v3a2 2 0 0 1-2 2A13 13 0 0 1 1 3a2 2 0 0 1 2-2z"/></svg>
        +65 6100 2040
      </li>
      <li>
        <svg viewBox="0 0 16 16" aria-hidden="true"><path d="M4 0h8a1 1 0 0 1 1 1v14a1 1 0 0 1-1 1H4a1 1 0 0 1-1-1V1a1 1 0 0 1 1-1zm1 2v10h6V2zm3 11a1 1 0 1 0 0 2 1 1 0 0 0 0-2z"/></svg>
        +65 9100 2200
      </li>
      <li>
        <svg viewBox="0 0 16 16" aria-hidden="true"><path d="M4 0h7v4H4zM1 5h14a1 1 0 0 1 1 1v6h-3v4H3v-4H0V6a1 1 0 0 1 1-1zm4 6v3h6v-3z"/></svg>
        +65 6100 2041
      </li>
      <li>
        <svg viewBox="0 0 16 16" aria-hidden="true"><path d="M0 3h16v1L8 9 0 4zm0 2.5 8 5 8-5V13H0z"/></svg>
        sales@nexalink.sg
      </li>
      <li>
        <svg viewBox="0 0 16 16" aria-hidden="true"><path d="M8 0a8 8 0 1 0 0 16A8 8 0 0 0 8 0zm-1 2v3H4.3A6 6 0 0 1 7 2zm2 0a6 6 0 0 1 2.7 3H9zM2.3 7H7v2H2.3a6 6 0 0 1 0-2zM9 7h4.7a6 6 0 0 1 0 2H9zm-4.7 4H7v3a6 6 0 0 1-2.7-3zM9 11h2.7A6 6 0 0 1 9 14z"/></svg>
        www.nexalink.sg
      </li>
    </ul>
  </section>

  <section class="card card-back">
    <div class="back-mark">
      <span class="brand-name">NEXALINK</span>
    </div>
    <ul class="tagline">
      <li class="lead">Industrial Networking &amp; Computing Specialist</li>
      <li>Industrial Ethernet / Wireless / Cellular</li>
      <li>Industrial &amp; Embedded Computing / Serial / Fieldbus Connectivity</li>
      <li>IP Video Surveillance / Remote Automation</li>
    </ul>
  </section>
</body>
</html>
```